New Business Card

Would like a shiny card with Metallic logo raised on th front. Address 418 Kestwick Lane, Toronto Ontario M4T2B8, phone 416 555 0382, email kmvc@lorentel.ca and web www.kmvc.ca on the back in right and left lower corners balanced. Top of back should say Thoughtful Care for Every Pet and Its Family centered. Leaving space on the back to write. Horizontal placement

```html
<!DOCTYPE html>
<html lang="en">
<head>
<meta charset="utf-8">
<title>Kestwick Lane Animal Hospital – Business Card</title>
<link rel="stylesheet" href="https://fonts.googleapis.com/css2?family=Exo+2:wght@500&family=Mulish:wght@400&display=swap">
<style>
  :root {
    --backdrop: #e0e0e2;
    --card: #ffffff;
    --ink: #1e1e20;
    --ink-soft: #3c3c40;
    --metal: #8a8a8c;
    --metal-light: #cfcfd1;
    --faint-mark: #f4f4f6;
    --rule: #4a4a4c;
  }
  html, body {
    margin: 0;
    padding: 0;
    width: 726px;
    height: 1200px;
    overflow: hidden;
    background: var(--backdrop);
  }
  .sheet {
    position: relative;
    width: 726px;
    height: 1200px;
  }
  .card {
    position: absolute;
    left: 96px;
    width: 534px;
    height: 303px;
    background: var(--card);
    border-radius: 17px;
    box-shadow: 0 2px 10px rgba(0,0,0,0.14);
    overflow: hidden;
  }
  .card--front { top: 96px; }
  .card--back-a { top: 448px; }
  .card--back-b { top: 800px; }

  /* front */
  .brand {
    position: absolute;
    left: 112px;
    width: 310px;
    top: 80px;
    text-align: center;
    font-family: "Exo 2", sans-serif;
    font-weight: 500;
    color: var(--metal);
  }
  .brand__dot {
    display: block;
    width: 92px;
    height: 92px;
    margin: 0 auto 14px;
    border-radius: 50%;
    background: linear-gradient(180deg, var(--metal-light), var(--metal));
  }
  .brand__name {
    display: block;
    font-size: 30px;
    letter-spacing: 2.4px;
    line-height: 1;
  }
  .brand__sub {
    display: flex;
    align-items: center;
    gap: 8px;
    margin-top: 3px;
    font-size: 13px;
    letter-spacing: 1.6px;
    line-height: 1;
  }
  .brand__sub::before,
  .brand__sub::after {
    content: "";
    flex: 1;
    height: 2px;
    background: var(--metal);
  }

  /* back */
  .faint-mark {
    position: absolute;
    left: 163px;
    top: 72px;
    width: 208px;
    height: 208px;
    border-radius: 50%;
    background: var(--faint-mark);
  }
  .tagline {
    position: absolute;
    left: 0; right: 0;
    margin: 0;
    text-align: center;
    font-family: "Exo 2", sans-serif;
    font-weight: 500;
    color: var(--ink);
  }
  .tagline__main { display: block; line-height: 1; }
  .tagline__sub {
    display: block;
    line-height: 1;
    color: var(--ink-soft);
  }
  .card--back-a .tagline { top: 34px; }
  .card--back-a .tagline__main { font-size: 31px; letter-spacing: 2.2px; }
  .card--back-a .tagline__sub { font-size: 16px; letter-spacing: 1px; margin-top: 2px; }

  .card--back-b .tagline { top: 32px; }
  .card--back-b .tagline__main { font-size: 40px; letter-spacing: 2.6px; }
  .tagline__sub--ruled {
    display: flex;
    align-items: center;
    gap: 10px;
    margin: 1px 31px 0;
    font-size: 17px;
    letter-spacing: 1.2px;
  }
  .tagline__sub--ruled::before,
  .tagline__sub--ruled::after {
    content: "";
    flex: 1;
    height: 2px;
    background: var(--rule);
  }

  .contact {
    position: absolute;
    left: 31px;
    width: 471px;
    top: 241px;
    border-top: 2px solid var(--rule);
    padding-top: 8px;
    text-align: center;
    font-family: "Mulish", sans-serif;
    font-size: 14px;
    line-height: 19px;
    color: var(--ink-soft);
  }
  .contact p { margin: 0; }
  .contact .sep { margin: 0 6px; }
</style>
</head>
<body>
<main class="sheet">

  <section class="card card--front" aria-label="Card front">
    <div class="brand">
      <span class="brand__dot"></span>
      <span class="brand__name">KESTWICK LANE</span>
      <span class="brand__sub">ANIMAL HOSPITAL</span>
    </div>
  </section>

  <section class="card card--back-a" aria-label="Card back, version one">
    <div class="faint-mark"></div>
    <h2 class="tagline">
      <span class="tagline__main">THOUGHTFUL CARE</span>
      <span class="tagline__sub">FOR EVERY PET AND ITS FAMILY</span>
    </h2>
    <div class="contact">
      <p>418 Kestwick Lane, Toronto Ontario M4T2B8</p>
      <p>416 555 0382<span class="sep">•</span>kmvc@lorentel.ca<span class="sep">•</span>www.kmvc.ca</p>
    </div>
  </section>

  <section class="card card--back-b" aria-label="Card back, version two">
    <div class="faint-mark"></div>
    <h2 class="tagline">
      <span class="tagline__main">THOUGHTFUL CARE</span>
      <span class="tagline__sub tagline__sub--ruled">FOR EVERY PET AND ITS FAMILY</span>
    </h2>
    <div class="contact">
      <p>418 Kestwick Lane, Toronto Ontario M4T2B8</p>
      <p>416 555 0382<span class="sep">•</span>kmvc@lorentel.ca<span class="sep">•</span>www.kmvc.ca</p>
    </div>
  </section>

</main>
</body>
</html>
```